Business card for acupunctist in Melbourne. Specialises in Fertility, pre and post natal care, pain

I am looking for a business card which is going to catch people eyes. Two sided, one side in a muted colour (keeping it feminine) (pink or yellow???)maybe with a little simple logo or picture, the other side I was thinking white with 3 colours (pink grey and yellow... Had these in mind.
Info on the card
Marla Quenby Acupuncture

Dr Marla Quenby (TCM Acupuncture)
Acupuncture for balancing body and mind.
Fernleaf Wellcraft
14 Corran Lane, Elsworth 3071.
94726150
0438219574
Marlatcm@quenbymail.com

Some other little logo/ designs I have liked are as follows:
http://www.dorisfelkaclinic.com/rates-and-insurance/
http://www.corinnetavish.com/
http://www.rz-needlework.co.uk/

Target Market(s)

professional women, people in pain, active people, people seeking a healthy lifefstyle.

Industry/Entity Type

Business

Font styles to use
Serif
Sans Serif

Colors
eea4c8
fde08a
aaaaaa

Requirements
Must have
• Must be eye catching, but not too loud and busy. Subltle is good. Simple is also good. The logo could be something that represents growth and health and nurturing. Again not too elaborate, very simple.
Thankyou
Should not have
• Electric colours, crazy fonts, Pictures of yin and yang, candles, or bodies.

```html
<!DOCTYPE html>
<html lang="en">
<head>
<meta charset="utf-8">
<title>Marla Quenby Acupuncture – Business Card</title>
<link href="https://fonts.googleapis.com/css2?family=Open+Sans:wght@400;700&family=Playfair+Display:wght@400&display=swap" rel="stylesheet">
<style>
  :root {
    --bg: #e9e9e9;
    --card: #ffffff;
    --pink: #eea4c8;
    --pink-deep: #e48fb9;
    --yellow: #fde08a;
    --grey: #aaaaaa;
    --ink: #2b2b2b;
    --ink-soft: #555555;
    --faint: #ececec;
  }
  * { margin: 0; padding: 0; box-sizing: border-box; }
  html, body { width: 1200px; height: 1200px; overflow: hidden; }
  body {
    background: var(--bg);
    font-family: "Open Sans", Arial, sans-serif;
    position: relative;
  }
  .card {
    position: absolute;
    left: 180px;
    width: 840px;
    height: 480px;
    background: var(--card);
    box-shadow: 0 6px 22px rgba(0,0,0,0.12);
    overflow: hidden;
  }
  .card--front { top: 90px; }
  .card--back { top: 630px; }

  .front-wave { position: absolute; inset: 0; }

  .brand {
    position: absolute;
    display: flex;
    align-items: center;
    gap: 16px;
    color: var(--pink-deep);
    font-family: "Playfair Display", Georgia, serif;
    font-weight: 400;
  }
  .brand__dot {
    width: 46px; height: 46px;
    border-radius: 50%;
    background: var(--pink);
    flex: none;
  }
  .brand__name { line-height: 1.1; }
  .card--front .brand { left: 370px; top: 205px; font-size: 36px; }
  .card--front .brand__name { width: 330px; }

  .holder {
    position: absolute;
    left: 60px; top: 58px;
  }
  .holder__name { font-size: 30px; font-weight: 700; color: var(--ink); }
  .holder__title { font-size: 18px; font-weight: 400; color: var(--ink-soft); }
  .holder__line { font-size: 18px; color: var(--ink-soft); line-height: 1.35; }

  .card--back .brand { left: 60px; top: 230px; font-size: 30px; }
  .card--back .brand__name { width: 280px; }
  .card--back .brand__dot { width: 40px; height: 40px; }

  .divider {
    position: absolute;
    left: 400px; top: 225px;
    width: 1px; height: 190px;
    background: var(--grey);
  }

  .contact {
    position: absolute;
    left: 425px; top: 228px;
    list-style: none;
    font-size: 21px;
    color: var(--ink);
  }
  .contact__item { display: flex; align-items: flex-start; gap: 12px; margin-bottom: 8px; line-height: 1.25; }
  .contact__icon {
    width: 24px; height: 24px; flex: none;
    border-radius: 50%;
    background: var(--pink);
    display: flex; align-items: center; justify-content: center;
    margin-top: 2px;
  }
  .contact__icon svg { width: 14px; height: 14px; fill: #fff; }

  .back-accent {
    position: absolute;
    right: -70px; top: 130px;
    width: 260px; height: 260px;
    border-radius: 50%;
    background: var(--faint);
    opacity: 0.8;
  }
</style>
</head>
<body>

<section class="card card--front" aria-label="Card front">
  <svg class="front-wave" viewBox="0 0 840 480" preserveAspectRatio="none">
    <path d="M0 0 H280 C250 120 330 210 350 300 C370 380 390 440 420 480 H0 Z" fill="var(--pink)"/>
    <path d="M280 0 C250 120 330 210 350 300 C370 380 390 440 420 480" fill="none" stroke="var(--yellow)" stroke-width="6"/>
  </svg>
  <div class="brand">
    <span class="brand__dot"></span>
    <span class="brand__name">Marla Quenby Acupuncture</span>
  </div>
</section>

<section class="card card--back" aria-label="Card back">
  <div class="back-accent"></div>

  <div class="holder">
    <p><span class="holder__name">Dr Marla Quenby</span> <span class="holder__title">(TCM Acupuncture)</span></p>
    <p class="holder__line">Acupuncture for balancing body and mind.</p>
    <p class="holder__line">Fernleaf Wellcraft</p>
  </div>

  <div class="brand">
    <span class="brand__dot"></span>
    <span class="brand__name">Marla Quenby Acupuncture</span>
  </div>

  <div class="divider"></div>

  <ul class="contact">
    <li class="contact__item">
      <span class="contact__icon"><svg viewBox="0 0 24 24"><path d="M12 2a7 7 0 0 0-7 7c0 5 7 13 7 13s7-8 7-13a7 7 0 0 0-7-7zm0 9.5A2.5 2.5 0 1 1 12 6.5a2.5 2.5 0 0 1 0 5z"/></svg></span>
      <span>14 Corran Lane,<br>Elsworth 3071.</span>
    </li>
    <li class="contact__item">
      <span class="contact__icon"><svg viewBox="0 0 24 24"><path d="M6.6 10.8a15 15 0 0 0 6.6 6.6l2.2-2.2a1 1 0 0 1 1-.25 11.4 11.4 0 0 0 3.6.57 1 1 0 0 1 1 1V20a1 1 0 0 1-1 1A17 17 0 0 1 3 4a1 1 0 0 1 1-1h3.5a1 1 0 0 1 1 1c0 1.25.2 2.45.57 3.57a1 1 0 0 1-.25 1z"/></svg></span>
      <span>94726150</span>
    </li>
    <li class="contact__item">
      <span class="contact__icon"><svg viewBox="0 0 24 24"><path d="M7 1h10a2 2 0 0 1 2 2v18a2 2 0 0 1-2 2H7a2 2 0 0 1-2-2V3a2 2 0 0 1 2-2zm0 3v14h10V4zm5 15.5a1 1 0 1 0 0 2 1 1 0 0 0 0-2z"/></svg></span>
      <span>0438219574</span>
    </li>
    <li class="contact__item">
      <span class="contact__icon"><svg viewBox="0 0 24 24"><path d="M2 5h20v14H2zm2 2v.5l8 5 8-5V7zm0 2.8V17h16V9.8l-8 5z"/></svg></span>
      <span>Marlatcm@quenbymail.com</span>
    </li>
  </ul>
</section>

</body>
</html>
```